Oven Cleaning flyer design

Hi there,
I need help designing a letterbox flyer. It needs to be DL size.
I have attached a rough design made with Chat GPT.
Would like back and front, have my business colors.
Please find attached mock up of what I would roughly like.
Also find attached logo.
Thank you

Target Market(s)

Home owners over 40

Industry/Entity Type

Cleaning

Requirements
Must have
• Logo, before after of oven, brand colors

```html
<!DOCTYPE html>
<html lang="en">
<head>
<meta charset="utf-8">
<title>Gleamhearth Oven Care – Flyer</title>
<link href="https://fonts.googleapis.com/css2?family=Poppins:wght@400;600;700;800&display=swap" rel="stylesheet">
<style>
  :root {
    --teal: #45c4cb;
    --ink: #0a0a0a;
    --body-text: #3a3a3a;
    --paper: #ffffff;
    --photo-dark: #1b2229;
    --photo-mid: #34404a;
    --photo-warm: #6b5434;
  }
  * { margin: 0; padding: 0; box-sizing: border-box; }
  html, body { width: 1200px; height: 2545px; overflow: hidden; background: var(--paper); }
  .flyer {
    position: relative;
    width: 1200px;
    height: 2545px;
    overflow: hidden;
    background: var(--paper);
    font-family: "Poppins", sans-serif;
  }
  .brand {
    position: absolute;
    top: 0; left: 0;
    width: 1200px; height: 297px;
    display: flex; align-items: center; justify-content: center;
    gap: 26px;
  }
  .brand-dot {
    width: 96px; height: 96px;
    border-radius: 50%;
    background: var(--teal);
  }
  .brand-name {
    font-weight: 700;
    font-size: 62px;
    color: var(--teal);
    letter-spacing: 1px;
  }
  .top-band {
    position: absolute;
    top: 297px; left: 0;
    width: 1200px; height: 21px;
    background: var(--teal);
  }
  .before-after {
    position: absolute;
    top: 318px; left: 0;
    width: 1200px; height: 972px;
    background: linear-gradient(90deg, var(--photo-warm) 0%, var(--photo-dark) 25%, var(--photo-mid) 50%, var(--photo-dark) 75%, var(--photo-mid) 100%);
  }
  .wave {
    position: absolute;
    top: 1100px; left: 0;
    width: 1200px; height: 200px;
  }
  .headline {
    position: absolute;
    top: 1365px; left: 0;
    width: 1200px;
    text-align: center;
    font-weight: 600;
    font-size: 160px;
    line-height: 138px;
    letter-spacing: -3px;
    color: var(--ink);
  }
  .headline .accent { color: var(--teal); }
  .intro {
    position: absolute;
    top: 1862px; left: 0;
    width: 1200px;
    text-align: center;
    font-weight: 400;
    font-size: 40px;
    line-height: 54px;
    color: var(--body-text);
  }
  .contact-band {
    position: absolute;
    top: 2197px; left: 0;
    width: 1200px; height: 348px;
    background: var(--ink);
  }
  .cta-pill {
    position: absolute;
    top: 2141px; left: 123px;
    width: 952px; height: 90px;
    border-radius: 45px;
    background: var(--teal);
    color: var(--paper);
    font-weight: 700;
    font-size: 40px;
    display: flex; align-items: center; justify-content: center;
  }
  .phone-row {
    position: absolute;
    top: 2250px; left: 0;
    width: 1200px; height: 150px;
    display: flex; align-items: center; justify-content: center;
    gap: 30px;
  }
  .phone-icon { width: 106px; height: 106px; }
  .phone-number {
    font-weight: 700;
    font-size: 136px;
    letter-spacing: -2px;
    color: var(--paper);
    line-height: 1;
  }
  .website {
    position: absolute;
    top: 2402px; left: 0;
    width: 1200px;
    text-align: center;
    font-weight: 400;
    font-size: 46px;
    letter-spacing: 2px;
    color: var(--teal);
  }
</style>
</head>
<body>
<div class="flyer">
  <header class="brand">
    <span class="brand-dot"></span>
    <span class="brand-name">Gleamhearth Oven Care</span>
  </header>

  <div class="top-band"></div>

  <div class="before-after" role="img" aria-label="Before and after photo of an oven interior: greasy, burnt oven on the left and a sparkling clean oven on the right"></div>

  <svg class="wave" viewBox="0 0 1200 200" aria-hidden="true">
    <path d="M0 64 C150 30 300 40 500 80 S1000 150 1200 110 L1200 200 L0 200 Z" fill="var(--teal)"/>
    <path d="M0 146 C150 100 350 95 600 150 S1050 200 1200 126 L1200 200 L0 200 Z" fill="var(--paper)"/>
  </svg>

  <h1 class="headline">Bring<br>Your <span class="accent">Oven</span><br>Back To Life</h1>

  <p class="intro">Professional, non-caustic oven cleaning that<br>removes built-up grease, smoke, and burnt<br>grime&nbsp; leaving your oven looking fresh again.</p>

  <div class="contact-band"></div>
  <div class="cta-pill">Call Now for Fast, Professional Service</div>

  <div class="phone-row">
    <svg class="phone-icon" viewBox="0 0 106 106" aria-hidden="true">
      <circle cx="53" cy="53" r="53" fill="var(--teal)"/>
      <path d="M38 28c3-2 6-1 7 2l5 10c1 3 0 5-2 6l-4 3c2 6 8 12 14 14l3-4c1-2 3-3 6-2l10 5c3 1 4 4 2 7l-3 5c-2 3-6 4-10 3-17-5-30-18-35-35-1-4 0-8 3-10z" fill="var(--paper)"/>
    </svg>
    <span class="phone-number">0400 583 219</span>
  </div>

  <div class="website">www.gleamhearthovencare.com.au</div>
</div>
</body>
</html>
```